Political Candidate Newspaper Advertisement

I would like a newspaper ad for my campaign for election to City Council. The banner ad is 10 cm high x 26.2 cm wide. The banner will contain a photo and the following text (or words to similar effect):
VOTE
DENNIS HALE
COMO BEACH
For a
SAFE
CARING
CONNECTED
COMMUNITY
Lifetime commitment to local clubs, charities and international aid
Local business owner
Founder of Open-Gate Week
Councillor, Mediator, B.Sc., MBA
The Councillor you know and can call for help
Respects our heritage and our future
Listens to the wisdom and needs of older residents
Promotes more young people
Protects our South Perth environment
Authorised by Dennis Hale 5/348 Kelby Rd, Como. 9317 2864
I use MS Publisher and PhotoShop so I'd like the product to be in a form I can use. After ther banner ad is done, and if it is good, I wish to pay the designer to use the same theme to produce another newspaper ad, a brochure and a poster.
My simple version is attached. A photo is also attached.
I'm hoping you do better.
18-80 years old
Business
- simple fonts
- A TICK somewhere around the word Vote would be good.
Mention of www.fairlandward.notepage.net if possible, perhaps at the bottom of the page, along with the Authorised by ... text.

```html
<!DOCTYPE html>
<html lang="en">
<head>
<meta charset="utf-8">
<title>Vote Dennis Hale – Como Beach</title>
<link rel="stylesheet" href="https://fonts.googleapis.com/css2?family=Source+Sans+3:wght@400;600;700;800&display=swap">
<style>
  :root {
    --navy: #2e3192;
    --red: #c1272d;
    --blue: #0b56a8;
    --blue-dark: #0a52a3;
    --ink: #2b2b2b;
    --grey-light: #f1f1f2;
    --grey-mid: #d6d7d9;
    --white: #ffffff;
  }
  * { margin: 0; padding: 0; box-sizing: border-box; }
  html, body { width: 1200px; height: 457px; overflow: hidden; background: var(--white); }
  body { font-family: "Source Sans 3", Arial, sans-serif; color: var(--ink); }

  .ad {
    position: relative;
    width: 1200px;
    height: 457px;
    overflow: hidden;
    background: linear-gradient(135deg, var(--grey-mid) 0%, var(--grey-light) 45%, var(--white) 85%);
  }

  .photo-panel {
    position: absolute;
    left: 906px; top: 0;
    width: 294px; height: 457px;
    background: var(--white);
    border-left: 3px solid var(--blue);
  }
  .candidate-photo {
    position: absolute;
    left: 930px; top: 22px;
    width: 270px; height: 435px;
    background: linear-gradient(180deg, #ead9cc 0%, #dcc4b2 32%, #4a4a4f 52%, #2a2a2e 100%);
  }

  .headline { position: absolute; left: 0; top: 0; width: 900px; height: 140px; }
  .headline__vote {
    position: absolute; left: 47px; top: 34px;
    font-size: 70px; font-weight: 800; color: var(--navy);
    line-height: 1; letter-spacing: 1px;
  }
  .vote-box {
    position: absolute; left: 230px; top: 33px;
    width: 96px; height: 96px;
    background: var(--white);
    box-shadow: 0 2px 6px rgba(0,0,0,0.18);
  }
  .headline__name {
    position: absolute; left: 337px; top: 32px;
    font-size: 70px; font-weight: 800; color: var(--red);
    line-height: 1; white-space: nowrap; letter-spacing: -0.3px;
  }
  .headline__ward {
    position: absolute; left: 341px; top: 101px;
    font-size: 37px; font-weight: 400; color: var(--ink);
    line-height: 1; white-space: nowrap;
  }

  .slogan {
    position: absolute; left: 47px; top: 148px;
    width: 673px; height: 39px;
    background: var(--blue);
    box-shadow: 0 7px 9px -5px rgba(0,0,0,0.35);
    color: var(--white);
    font-size: 29px; font-weight: 700; font-variant: small-caps;
    line-height: 39px; padding-left: 20px; white-space: nowrap;
  }
  .slogan__dot { margin: 0 9px; font-size: 18px; vertical-align: 4px; }

  .points { position: absolute; list-style: none; font-size: 19.4px; line-height: 22px; color: var(--ink); }
  .points--left { left: 48px; top: 221px; width: 340px; }
  .points--right { left: 402px; top: 221px; width: 480px; }
  .points li { position: relative; padding-left: 29px; margin-bottom: 7px; white-space: nowrap; }
  .points li svg { position: absolute; left: 0; top: 4px; }

  .footer-bar {
    position: absolute; left: 0; top: 412px;
    width: 906px; height: 45px;
    background: var(--blue-dark);
    color: var(--white);
    white-space: nowrap;
  }
  .footer-bar__web { position: absolute; left: 47px; top: 11px; font-size: 18px; font-weight: 700; }
  .footer-bar__auth { position: absolute; left: 410px; top: 11px; font-size: 18.5px; font-weight: 400; }
</style>
</head>
<body>
<main class="ad">
  <div class="photo-panel"></div>
  <div class="candidate-photo" role="img" aria-label="Portrait photo of the candidate in a dark suit and tie"></div>

  <header class="headline">
    <span class="headline__vote">VOTE</span>
    <span class="vote-box" aria-hidden="true"></span>
    <h1 class="headline__name">DENNIS HALE</h1>
    <p class="headline__ward">COMO BEACH</p>
  </header>

  <p class="slogan">For a Safe<span class="slogan__dot">•</span>Caring<span class="slogan__dot">•</span>Connected<span class="slogan__dot">•</span>Community</p>

  <ul class="points points--left">
    <li><svg width="14" height="14" viewBox="0 0 14 14" aria-hidden="true"><rect x="1" y="1" width="12" height="12" fill="none" stroke="#2e3192" stroke-width="1.6"/><path d="M3.5,7 L6,10 L11,3.5" fill="none" stroke="#2e3192" stroke-width="2"/></svg>Lifetime commitment to local clubs,<br>charities and international aid</li>
    <li><svg width="14" height="14" viewBox="0 0 14 14" aria-hidden="true"><rect x="1" y="1" width="12" height="12" fill="none" stroke="#2e3192" stroke-width="1.6"/><path d="M3.5,7 L6,10 L11,3.5" fill="none" stroke="#2e3192" stroke-width="2"/></svg>Local business owner</li>
    <li><svg width="14" height="14" viewBox="0 0 14 14" aria-hidden="true"><rect x="1" y="1" width="12" height="12" fill="none" stroke="#2e3192" stroke-width="1.6"/><path d="M3.5,7 L6,10 L11,3.5" fill="none" stroke="#2e3192" stroke-width="2"/></svg>Founder of Open-Gate Week</li>
    <li><svg width="14" height="14" viewBox="0 0 14 14" aria-hidden="true"><rect x="1" y="1" width="12" height="12" fill="none" stroke="#2e3192" stroke-width="1.6"/><path d="M3.5,7 L6,10 L11,3.5" fill="none" stroke="#2e3192" stroke-width="2"/></svg>Councillor, Mediator, B.Sc., MBA</li>
  </ul>

  <ul class="points points--right">
    <li><svg width="14" height="14" viewBox="0 0 14 14" aria-hidden="true"><rect x="1" y="1" width="12" height="12" fill="none" stroke="#2e3192" stroke-width="1.6"/><path d="M3.5,7 L6,10 L11,3.5" fill="none" stroke="#2e3192" stroke-width="2"/></svg>The Councillor you know and can call for help</li>
    <li><svg width="14" height="14" viewBox="0 0 14 14" aria-hidden="true"><rect x="1" y="1" width="12" height="12" fill="none" stroke="#2e3192" stroke-width="1.6"/><path d="M3.5,7 L6,10 L11,3.5" fill="none" stroke="#2e3192" stroke-width="2"/></svg>Respects our heritage and our future</li>
    <li><svg width="14" height="14" viewBox="0 0 14 14" aria-hidden="true"><rect x="1" y="1" width="12" height="12" fill="none" stroke="#2e3192" stroke-width="1.6"/><path d="M3.5,7 L6,10 L11,3.5" fill="none" stroke="#2e3192" stroke-width="2"/></svg>Listens to the wisdom and needs of older residents</li>
    <li><svg width="14" height="14" viewBox="0 0 14 14" aria-hidden="true"><rect x="1" y="1" width="12" height="12" fill="none" stroke="#2e3192" stroke-width="1.6"/><path d="M3.5,7 L6,10 L11,3.5" fill="none" stroke="#2e3192" stroke-width="2"/></svg>Promotes more young people</li>
    <li><svg width="14" height="14" viewBox="0 0 14 14" aria-hidden="true"><rect x="1" y="1" width="12" height="12" fill="none" stroke="#2e3192" stroke-width="1.6"/><path d="M3.5,7 L6,10 L11,3.5" fill="none" stroke="#2e3192" stroke-width="2"/></svg>Protects our South Perth environment</li>
  </ul>

  <footer class="footer-bar">
    <span class="footer-bar__web">www.fairlandward.notepage.net</span>
    <span class="footer-bar__auth">Authorised by Dennis Hale 5/348 Kelby Rd, Como. 9317 2864</span>
  </footer>
</main>
</body>
</html>
```